KEP Business Card

the business card should be double sided.
Will need to be Korean on one side and english on the other.
it will need to have:

address
website
skype
phone
cell
fax
name
title
email

just put in dummy details to start - i will then give you correct info once we have the format right.

Also - if you feel creative about the logo we are happy to make some amendments to it so it looks right. We are still at early stages with the logo so happy if you have suggestions around the logo concept.
Updates

The deadline for this has been brought forward to Wednesday 11th December. We can not review any designs after this date.

we will need to make a decision by Wednesday 11th December, so please have designs in by this date and not by the deadline set by lumahive

Target Market(s)

large companies, executives

Industry/Entity Type

Business

Colors

Designer to choose colors to be used in the design.

Requirements
Must have
• double sided - english on one side and korean on the other. we will give you korean wording once we have a design we like.

```html
<!DOCTYPE html>
<html lang="en">
<head>
<meta charset="utf-8">
<title>KEP Business Card</title>
<link rel="stylesheet" href="https://fonts.googleapis.com/css2?family=Tinos:wght@400;700&display=swap">
<style>
  :root {
    --backdrop: #e8e8ea;
    --card-black: #0b0b0c;
    --accent-blue: #1a4fa3;
    --text-white: #f2f2f2;
    --text-grey: #b9b9bb;
    --rule-grey: #6c6c70;
  }
  * { margin: 0; padding: 0; box-sizing: border-box; }
  html, body {
    width: 1200px; height: 835px; overflow: hidden;
    background: var(--backdrop);
    font-family: "Tinos", "Times New Roman", serif;
  }
  .card {
    position: absolute; left: 100px; top: 131px;
    width: 1000px; height: 572px;
    background: var(--card-black);
    box-shadow: 0 14px 30px rgba(0,0,0,0.18);
    overflow: hidden;
  }
  .accent-band {
    position: absolute; left: 0; right: 0; bottom: 0; height: 30px;
    background: var(--accent-blue);
  }
  .rule { position: absolute; background: var(--rule-grey); }
  .rule-top { left: 150px; top: 200px; width: 170px; height: 2px; }
  .rule-divider { left: 330px; top: 245px; width: 2px; height: 230px; }
  .rule-bottom { left: 342px; top: 474px; width: 210px; height: 2px; }
  .business-name {
    position: absolute; left: 345px; top: 172px;
    color: var(--text-white); font-size: 38px; font-weight: 400; line-height: 1;
  }
  .brand {
    position: absolute; left: 150px; top: 285px;
    display: flex; align-items: center; gap: 12px;
  }
  .brand-square { width: 20px; height: 20px; background: var(--accent-blue); }
  .brand-name { color: var(--accent-blue); font-size: 34px; font-weight: 400; letter-spacing: 2px; line-height: 1; }
  .person { position: absolute; left: 110px; top: 385px; width: 210px; }
  .person-name { color: var(--text-white); font-size: 34px; font-weight: 400; letter-spacing: 1px; line-height: 1.1; white-space: nowrap; }
  .person-title { color: var(--text-grey); font-size: 14px; letter-spacing: 1px; margin-top: 4px; }
  .contact {
    position: absolute; left: 352px; top: 252px;
    color: var(--text-grey); font-size: 19px; line-height: 29px; font-style: normal;
    white-space: nowrap;
  }
  .contact .sep { margin: 0 6px; }
</style>
</head>
<body>
  <section class="card" aria-label="KEP business card, English side">
    <div class="rule rule-top"></div>
    <div class="rule rule-divider"></div>
    <div class="rule rule-bottom"></div>

    <h1 class="business-name">Business Name</h1>

    <div class="brand">
      <span class="brand-square"></span>
      <span class="brand-name">KEP</span>
    </div>

    <div class="person">
      <p class="person-name">FULL NAME</p>
      <p class="person-title">TITLE SAMPLE TEXT</p>
    </div>

    <address class="contact">
      <p>2450 Harbor Lane, Suite 305, Fairview, OR 97215</p>
      <p>phone: 555.318.2046<span class="sep">|</span>cell: 555.907.6621</p>
      <p>fax: 555.318.2047<span class="sep">|</span>skype: kepoffice</p>
      <p>email: hello@kep.example<span class="sep">|</span>website: kep.example</p>
    </address>

    <div class="accent-band"></div>
  </section>
</body>
</html>
```